Wine label refresh

We are wanting to modify our Corran Estate label to include a picture on it.
I have attached the pictures below which we would like on the label. They are of the Corran Estate vineyard. I have also attached an example of another label with a picture on it that we like the style of.
Industry/Entity Type
Vineyard
Requirements
Must have
- The Corran Estate text must stay the same but can be moved down. It still needs to be the same size though.
Marlborough Sauvignon Blanc should remain in the same font and roughly the same size.
Wine of New Zealand also must stay but could potentially be moved.
Nice to have
- It would be nice if we could keep the KL logo on the front label but feel free to experiment with where this goes.

```html
<!DOCTYPE html>
<html lang="en">
<head>
<meta charset="utf-8">
<title>Corran Estate – Marlborough Sauvignon Blanc Label</title>
<link rel="stylesheet" href="https://fonts.googleapis.com/css2?family=Cormorant+Garamond:wght@500&family=Pinyon+Script&family=Open+Sans:wght@400&family=Tinos&display=swap">
<style>
  :root {
    --paper: #ffffff;
    --frame: #6f6f73;
    --edge: #c9c9cc;
    --estate-blue: #1c2bc4;
    --navy: #141a4e;
    --band-glow: #3048dc;
    --silver: #a3a4b2;
    --vintage-blue: #1f2fc8;
    --band-text: #e3e4ec;
    --orange: #f2992e;
    --photo-light: #d3d8f3;
    --photo-mid: #9ea8df;
    --photo-deep: #6b77c2;
  }
  * { margin: 0; padding: 0; box-sizing: border-box; }
  html, body { width: 1036px; height: 1200px; overflow: hidden; background: var(--paper); }
  .label {
    position: relative;
    width: 1036px;
    height: 1200px;
    background: var(--paper);
    border: 1px solid var(--edge);
    overflow: hidden;
  }
  .rule {
    position: absolute;
    left: 371px;
    width: 314px;
    height: 2px;
    background: var(--estate-blue);
  }
  .rule--top { top: 112px; }
  .rule--bottom { top: 337px; }
  .monogram {
    position: absolute;
    top: 128px;
    left: 0;
    width: 1036px;
    text-align: center;
    font-family: "Cormorant Garamond", serif;
    font-weight: 500;
    font-size: 84px;
    line-height: 96px;
    color: var(--estate-blue);
  }
  .estate-name {
    position: absolute;
    top: 252px;
    left: 0;
    width: 1036px;
    text-align: center;
    font-family: "Cormorant Garamond", serif;
    font-weight: 500;
    font-size: 66px;
    line-height: 70px;
    letter-spacing: 3px;
    font-variant: small-caps;
    color: var(--estate-blue);
  }
  .vineyard-photo {
    position: absolute;
    left: 224px;
    top: 374px;
    width: 598px;
    height: 370px;
    background: linear-gradient(180deg, var(--photo-light) 0%, var(--photo-mid) 45%, var(--photo-deep) 100%);
  }
  .varietal-band {
    position: absolute;
    left: 0;
    top: 785px;
    width: 1036px;
    height: 272px;
    background: radial-gradient(ellipse 420px 230px at 50% 40%, var(--band-glow) 0%, #2436b4 40%, var(--navy) 100%);
  }
  .vintage {
    position: absolute;
    top: 106px;
    left: 0;
    width: 1036px;
    text-align: center;
    font-family: "Tinos", serif;
    font-size: 82px;
    line-height: 82px;
    color: var(--vintage-blue);
  }
  .varietal {
    position: absolute;
    top: 60px;
    left: 0;
    width: 1036px;
    text-align: center;
    font-family: "Pinyon Script", cursive;
    font-size: 80px;
    line-height: 110px;
    color: var(--silver);
    white-space: nowrap;
  }
  .volume, .strength {
    position: absolute;
    top: 225px;
    font-family: "Open Sans", sans-serif;
    font-size: 34px;
    line-height: 40px;
    color: var(--band-text);
  }
  .volume { left: 40px; }
  .strength { right: 40px; }
  .origin-band {
    position: absolute;
    left: 0;
    top: 1057px;
    width: 1036px;
    height: 92px;
    background: var(--orange);
    display: flex;
    align-items: center;
    justify-content: center;
    font-family: "Open Sans", sans-serif;
    font-size: 41px;
    letter-spacing: 1px;
    color: var(--paper);
  }
  .frame {
    position: absolute;
    left: 0;
    top: 0;
    width: 1036px;
    height: 1200px;
    pointer-events: none;
  }
</style>
</head>
<body>
  <main class="label">
    <div class="rule rule--top"></div>
    <div class="monogram">KL</div>
    <h1 class="estate-name">Corran Estate</h1>
    <div class="rule rule--bottom"></div>

    <div class="vineyard-photo" role="img" aria-label="Blue-toned photograph of the Corran Estate vineyard: rows of vines, palm trees and a house with hills behind"></div>

    <section class="varietal-band">
      <div class="vintage">2012</div>
      <h2 class="varietal">Marlborough Sauvignon Blanc</h2>
      <span class="volume">750ml</span>
      <span class="strength">13%acl/vol</span>
    </section>

    <div class="origin-band">WINE OF NEW ZEALAND</div>

    <svg class="frame" viewBox="0 0 1036 1200" aria-hidden="true">
      <rect x="28" y="32" width="983" height="1142" rx="14" ry="14" fill="none" stroke="var(--frame)" stroke-width="3"/>
    </svg>
  </main>
</body>
</html>
```